Door Company Flyer for October Hardware Sale

We are a door company and need a new flyer for a sale on hardware going on starting today thru the end of October (Oct 1st-Oct 31st) Our logo colors are gray, orange, and white. We need the 3 pictures of hardware included. Our company is TALVO Commercial Door, our supplier is Quorvane and the hardware on sale is Marten brand. We will need this in pdf format to print flyers and also a digital version to post on our website and social media.

```html
<!DOCTYPE html>
<html lang="en">
<head>
<meta charset="utf-8">
<title>TALVO Commercial Door – October Hardware Sale</title>
<link rel="stylesheet" href="https://fonts.googleapis.com/css2?family=Oswald:wght@300;400;600;700&family=Montserrat:wght@600;700;800&family=Open+Sans:wght@400;600&display=swap">
<style>
  :root {
    --orange: #f5931f;
    --gray: #8e8f92;
    --gray-dark: #58595b;
    --ink: #2b2b2b;
    --paper: #ffffff;
    --paper-tint: #f1f1f2;
    --stage: #7f7f80;
  }
  * { box-sizing: border-box; margin: 0; padding: 0; }
  html, body { width: 1200px; height: 951px; overflow: hidden; background: var(--stage); }
  .flyer {
    position: absolute; left: 232px; top: 0; width: 735px; height: 951px;
    background: linear-gradient(160deg, var(--paper-tint) 0%, var(--paper) 45%, var(--paper-tint) 100%);
    overflow: hidden; font-family: "Open Sans", sans-serif; color: var(--gray-dark);
  }
  .shapes { position: absolute; inset: 0; }
  .brand { position: absolute; left: 40px; top: 48px; display: flex; align-items: center; gap: 10px; }
  .brand-mark { width: 26px; height: 26px; background: var(--orange); }
  .brand-name { font-family: "Oswald", sans-serif; font-weight: 600; font-size: 30px; letter-spacing: 2px; color: var(--gray-dark); line-height: 1; }
  .brand-sub { font-family: "Oswald", sans-serif; font-weight: 600; font-size: 11px; letter-spacing: 1.5px; color: var(--gray-dark); }
  .headline { position: absolute; left: 72px; top: 160px; font-family: "Oswald", sans-serif; color: var(--paper); text-transform: uppercase; line-height: 1.08; }
  .headline .light { font-weight: 300; font-size: 38px; display: block; }
  .headline .bold { font-weight: 700; font-size: 46px; display: block; }
  .sale-tag { position: absolute; left: 66px; top: 612px; background: var(--orange); color: var(--paper); font-family: "Oswald", sans-serif; font-weight: 400; font-size: 27px; padding: 2px 14px; text-transform: uppercase; }
  .sale-dates { position: absolute; left: 70px; top: 660px; font-family: "Oswald", sans-serif; font-size: 32px; color: var(--orange); font-weight: 400; }
  .sale-dates .to { color: var(--gray-dark); font-size: 26px; }
  .services { position: absolute; left: 70px; top: 725px; width: 340px; list-style: none; }
  .service { display: flex; gap: 14px; margin-bottom: 14px; align-items: flex-start; }
  .service svg { width: 32px; height: 32px; flex: none; margin-top: 6px; }
  .service h3 { font-family: "Montserrat", sans-serif; font-weight: 700; font-size: 17px; color: var(--orange); line-height: 1.2; }
  .service p { font-size: 10.5px; line-height: 1.35; color: var(--gray-dark); }
  .contact { position: absolute; left: 440px; top: 610px; width: 295px; height: 200px; background: var(--gray); color: var(--paper); padding: 22px 24px; }
  .contact h2 { font-family: "Montserrat", sans-serif; font-weight: 700; font-size: 18px; padding-bottom: 6px; border-bottom: 2px solid var(--orange); display: inline-block; margin-bottom: 12px; }
  .contact ul { list-style: none; }
  .contact li { display: flex; gap: 9px; font-size: 14px; line-height: 1.3; margin-bottom: 6px; }
  .contact li svg { width: 13px; height: 13px; flex: none; margin-top: 3px; fill: var(--paper); }
  .contact li svg.icon-web { fill: none; }
  .partners { position: absolute; left: 440px; width: 265px; top: 858px; display: flex; gap: 24px; align-items: center; justify-content: flex-end; }
  .partner { font-family: "Montserrat", sans-serif; font-weight: 800; font-size: 22px; color: var(--ink); display: flex; align-items: center; gap: 8px; white-space: nowrap; }
  .partner-square { width: 18px; height: 18px; background: var(--orange); }
</style>
</head>
<body>
<main class="flyer">
  <svg class="shapes" viewBox="0 0 735 951" width="735" height="951">
    <defs>
      <linearGradient id="room" x1="0" y1="0" x2="0" y2="1">
        <stop offset="0" stop-color="#2f3135"/><stop offset="0.4" stop-color="#d9d9d9"/><stop offset="1" stop-color="#8e8e8c"/>
      </linearGradient>
      <linearGradient id="hardware" x1="0" y1="0" x2="1" y2="1">
        <stop offset="0" stop-color="#9a9a9a"/><stop offset="1" stop-color="#5a5a5a"/>
      </linearGradient>
    </defs>
    <polygon class="hero-photo" role="img" aria-label="Photo of an empty commercial interior with grey doors" points="290,0 735,0 735,300 450,332" fill="url(#room)"/>
    <polygon class="headline-band" points="40,125 335,125 455,312 40,415" fill="var(--orange)"/>
    <polygon class="product-frame" points="55,380 700,372 700,592 55,598" fill="var(--orange)"/>
    <polygon class="product-photo" role="img" aria-label="Photo of door strike plates and lock cylinders" points="65,390 280,388 316,586 65,588" fill="url(#hardware)"/>
    <polygon class="product-photo" role="img" aria-label="Photo of a door closer arm" points="292,388 490,385 526,584 328,586" fill="url(#hardware)"/>
    <polygon class="product-photo" role="img" aria-label="Photo of a lever lockset with keys" points="502,385 690,382 690,582 538,584" fill="url(#hardware)"/>
  </svg>

  <div class="brand">
    <span class="brand-mark"></span>
    <div><div class="brand-name">TALVO</div><div class="brand-sub">COMMERCIAL DOOR</div></div>
  </div>

  <h1 class="headline">
    <span class="light">We take pride</span>
    <span class="light">in providing</span>
    <span class="bold">High quality</span>
    <span class="bold">hardware</span>
  </h1>

  <div class="sale-tag">Sale start today</div>
  <div class="sale-dates">1St October <span class="to">to</span> 31st october</div>

  <ul class="services">
    <li class="service">
      <svg viewBox="0 0 32 32" fill="none" stroke="var(--orange)" stroke-width="2"><path d="M3 18l7-6h6l4 3 5-3 4 4-9 8h-7l-5-3z"/><circle cx="24" cy="8" r="4"/></svg>
      <div><h3>Sales</h3><p>We always aim for customer satisfaction when selling our products and services to our customers.</p></div>
    </li>
    <li class="service">
      <svg viewBox="0 0 32 32" fill="none" stroke="var(--orange)" stroke-width="3"><circle cx="16" cy="16" r="6"/><path d="M16 3v5M16 24v5M3 16h5M24 16h5M7 7l3.5 3.5M21.5 21.5L25 25M7 25l3.5-3.5M21.5 10.5L25 7"/></svg>
      <div><h3>Service</h3><p>Have an existing commercial door that is in need of repair? Contact us for a service call.</p></div>
    </li>
    <li class="service">
      <svg viewBox="0 0 32 32" fill="var(--orange)"><path d="M22 3a7 7 0 0 0-6.6 9.3L4 23.7 8.3 28l11.4-11.4A7 7 0 0 0 29 10l-4 4-4-1-1-4 4-4a7 7 0 0 0-2-2z"/></svg>
      <div><h3>Installation</h3><p>Apart from providing Doors, Frames, and Hardware, we can also provide installation if needed.</p></div>
    </li>
  </ul>

  <section class="contact">
    <h2>Contact Us Today</h2>
    <ul>
      <li><svg viewBox="0 0 16 16"><path d="M3 1l3 3-2 2a9 9 0 0 0 6 6l2-2 3 3-2 2C7 15 1 9 1 3z"/></svg>(555) 210-4477</li>
      <li><svg viewBox="0 0 16 16"><circle cx="8" cy="8" r="7"/><path d="M8 4v4h3" stroke="var(--gray)" stroke-width="1.6" fill="none"/></svg>Mon - Fri 8:00 - 5:00</li>
      <li><svg viewBox="0 0 16 16"><path d="M8 1a5 5 0 0 0-5 5c0 4 5 9 5 9s5-5 5-9a5 5 0 0 0-5-5zm0 7a2 2 0 1 1 0-4 2 2 0 0 1 0 4z"/></svg>418 W Alder St Ste B,<br>Harlow Tx.</li>
      <li><svg class="icon-web" viewBox="0 0 16 16" stroke="#fff" stroke-width="1.3"><circle cx="8" cy="8" r="6.5"/><path d="M1.5 8h13M8 1.5c-3 3.5-3 9.5 0 13M8 1.5c3 3.5 3 9.5 0 13"/></svg>talvocommercialdoor.com</li>
    </ul>
  </section>

  <div class="partners">
    <span class="partner">Marten</span>
    <span class="partner"><span class="partner-square"></span>QUORVANE</span>
  </div>
</main>
</body>
</html>
```